Marlowick Investment Partners Website | ||
Financial Services | ||
mipfundexample.com | ||
The company is an investment fund. The site must inspire trust and confidence yet have style. It must be VERY professional. | ||
I like things simple and elegant. Rich and classy in appearance. I don't care too much about colors, but it's probably easiest to use the colors already used in my logos. | ||
Clean/Simple Professional Content Driven Conservative Sophisticated Corporate Modern Elegant Traditional Masculine |
left side | ||
https://www.castrelfunds.example/cm/Satellite?pagename=cfVanityWrapper&UserFriendlyURL=home | ||
http://www.tuvrelle.example/ | ||
http://www2.pinegate.example/US/individual-investors | ||
The site doesn't need to be terribly complex nor work as a stand-alone source for sales. It is mainly a source for further information for people I have talked to about the fund personally. It should also be a place for current clients to check on performance of their portfolios. Of the websites listed above: I like Castrel Banks's appearance I like Tuvrelle's layout and simplicity pinegate I like in general I also made a mock up of how i saw the site, which I'll upload once the contest is up and running. |

```html
<!DOCTYPE html>
<html lang="en">
<head>
<meta charset="utf-8">
<title>Marlowick Investment Partners — Client Log-in</title>
<link rel="stylesheet" href="https://fonts.googleapis.com/css2?family=Cinzel:wght@400&family=Cormorant+Garamond:ital,wght@1,500&family=Oswald:wght@400&family=Open+Sans:wght@400&display=swap">
<style>
  :root {
    --header-top: #2a2a2a;
    --header-bottom: #121212;
    --body-bg: #222222;
    --footer-bg: #161616;
    --teal: #3fa9b5;
    --teal-dark: #1d5860;
    --teal-light: #7fd0da;
    --text: #bdbdbd;
    --text-dim: #7d7d7d;
    --heading: #d8d8d8;
    --field: #0b0b0b;
    --field-border: #3a3a3a;
    --white: #f2f2f2;
  }
  * { box-sizing: border-box; margin: 0; padding: 0; }
  html, body { width: 1200px; height: 720px; overflow: hidden; background: var(--body-bg); }
  .page { position: relative; width: 1200px; height: 720px; font-family: "Open Sans", sans-serif; color: var(--text); }

  .site-header {
    position: absolute; left: 0; top: 0; width: 1200px; height: 160px;
    background: linear-gradient(180deg, var(--header-top), var(--header-bottom));
    border-bottom: 1px solid #050505;
  }
  .brand { position: absolute; left: 132px; top: 29px; display: flex; align-items: center; gap: 18px; }
  .brand-mark { width: 84px; height: 84px; background: var(--teal); }
  .brand-name { font-family: "Cinzel", serif; color: var(--teal); line-height: 1; }
  .brand-name .primary { display: block; font-size: 50px; letter-spacing: 1px; }
  .brand-name .secondary { display: block; font-size: 15px; letter-spacing: 2.5px; margin-top: 8px; }
  .tagline {
    position: absolute; left: 796px; top: 52px; width: 340px;
    font-family: "Cormorant Garamond", serif; font-style: italic; font-weight: 500;
    font-size: 31px; line-height: 1.05; color: var(--white); text-align: center;
  }
  .tagline .quote { color: var(--teal); }

  .vault-photo {
    position: absolute; left: 144px; top: 240px; width: 355px; height: 257px;
    border: 8px solid #0c0c0c;
    background: radial-gradient(circle at 62% 45%, #b9b9b9 0%, #7d7d7d 30%, #3b3b3b 60%, #151515 100%);
  }

  .login { position: absolute; left: 557px; top: 262px; width: 480px; }
  .login-title { font-family: "Oswald", sans-serif; font-size: 24px; letter-spacing: 1px; color: var(--heading); text-transform: uppercase; }
  .login-title .divider { color: var(--text-dim); margin: 0 10px; }
  .fields { display: flex; gap: 14px; margin-top: 14px; align-items: flex-end; }
  .field label { display: block; font-size: 13px; color: var(--text); margin-bottom: 4px; }
  .field .input { height: 24px; background: var(--field); border: 1px solid var(--field-border); }
  .field.username .input { width: 204px; }
  .field.password .input { width: 214px; }
  .submit {
    width: 36px; height: 24px; background: var(--field); border: 1px solid var(--field-border);
    display: flex; align-items: center; justify-content: center; margin-left: -7px;
  }
  .reset { font-size: 13px; margin-top: 12px; }
  .reset a { color: var(--teal); text-decoration: none; }
  .address { font-size: 12.5px; line-height: 18px; margin-top: 36px; color: var(--text); font-style: normal; }

  .site-footer {
    position: absolute; left: 0; top: 610px; width: 1200px; height: 110px;
    background: linear-gradient(180deg, #1a1a1a, var(--footer-bg));
  }
  .footer-rule { position: absolute; left: 557px; top: 0; width: 475px; height: 2px; background: var(--teal-dark); }
  .copyright { position: absolute; left: 139px; top: 17px; font-size: 12.5px; color: var(--text-dim); }
  .enter-site {
    position: absolute; left: 919px; top: 2px; width: 113px; height: 34px;
    background: var(--teal-dark); color: var(--teal-light);
    font-family: "Oswald", sans-serif; font-size: 17px; letter-spacing: 1px;
    display: flex; align-items: center; justify-content: center; text-transform: uppercase;
  }
</style>
</head>
<body>
<div class="page">
  <header class="site-header">
    <div class="brand">
      <div class="brand-mark"></div>
      <div class="brand-name">
        <span class="primary">MARLOWICK</span>
        <span class="secondary">INVESTMENT PARTNERS</span>
      </div>
    </div>
    <p class="tagline"><span class="quote">“</span>Hedge Fund Strategies at Mutual Fund Prices<span class="quote">”</span></p>
  </header>

  <main>
    <div class="vault-photo" role="img" aria-label="Photograph of an open steel bank vault door"></div>

    <section class="login">
      <h1 class="login-title">Client Log-in<span class="divider">|</span>Sign Up</h1>
      <div class="fields">
        <div class="field username"><label>User Name:</label><div class="input"></div></div>
        <div class="field password"><label>Password:</label><div class="input"></div></div>
        <div class="submit">
          <svg width="16" height="10" viewBox="0 0 16 10"><rect x="1" y="2" width="8" height="6" rx="3" fill="none" stroke="#bdbdbd" stroke-width="1.6"/><rect x="7" y="2" width="8" height="6" rx="3" fill="none" stroke="#bdbdbd" stroke-width="1.6"/></svg>
        </div>
      </div>
      <p class="reset">Have you forgotten your password? Reset it <a href="#">here</a>.</p>
      <address class="address">
        Marlowick Investment Partners<br>
        48 Harrow Lane, Suite 900<br>
        Ashbury, MA 02190<br>
        Tel: 555-014-2290
      </address>
    </section>
  </main>

  <footer class="site-footer">
    <div class="footer-rule"></div>
    <p class="copyright">© Marlowick Investment Partners, All Rights Reserved, 2011</p>
    <a class="enter-site">Enter Site</a>
  </footer>
</div>
</body>
</html>
```